Meadow Reset sale graphics for social media

You MUST read the Brief in the WORD document and follow the instructions there. I want to create 10 social media graphics (new Instagram size 4:5 (1080 x 1350 pixels) focusing on our Mother’s Day Meadow Reset Sale graphics, using any of the pics attached. Use the attached pics, NO RANDOM STOCK PHOTOGRAPHY. For the color scheme of the graphics, they should all be complementary to the product colors or feel like Spring time.

Target Market(s)

primarily women

Requirements
Must have
• the photos and text attached

```html
<!DOCTYPE html>
<html lang="en">
<head>
<meta charset="utf-8">
<title>Meadow Reset Sale — Social Graphics</title>
<link rel="stylesheet" href="https://fonts.googleapis.com/css2?family=Jost:wght@500&family=Poppins:wght@700;800&display=swap">
<style>
  :root {
    --page: #ffffff;
    --rose: #c9689f;
    --rose-soft: #dc86ad;
    --rose-deep: #a95a8c;
    --mint: #a3cfc4;
    --mint-deep: #6fa596;
    --white: #ffffff;
    --tint-pink: #e3b3d3;
    --tint-red: #e79a9a;
    --tint-green: #a9cfc0;
    --tint-blue: #a9b3dc;
  }
  * { box-sizing: border-box; margin: 0; padding: 0; }
  html, body { width: 1200px; height: 2182px; overflow: hidden; background: var(--page); }
  .canvas { position: relative; width: 1200px; height: 2182px; }

  .tile { position: absolute; width: 504px; height: 630px; overflow: hidden; }
  .col-left { left: 54px; }
  .col-right { left: 643px; }
  .row-1 { top: 54px; }
  .row-2 { top: 772px; }
  .row-3 { top: 1491px; }

  .header {
    position: absolute; left: 0; top: 0; width: 100%; z-index: 2;
    display: flex; flex-direction: column; justify-content: center; align-items: center;
    font-family: "Jost", sans-serif; font-weight: 500; color: var(--white);
    text-transform: uppercase; text-align: center;
    letter-spacing: 0.17em; line-height: 1.22;
  }
  .header--rose { background: var(--rose); }
  .header--rose-soft { background: var(--rose-soft); }
  .header--mint { background: var(--mint); }

  .photo { position: absolute; left: 0; width: 100%; bottom: 0; }
  .photo--studio {
    background:
      linear-gradient(180deg, rgba(255,255,255,0) 0%, rgba(255,255,255,0) 62%, rgba(205,205,210,0.55) 63%, rgba(236,236,238,0.2) 100%),
      linear-gradient(180deg, #efeff1 0%, #e4e4e7 100%);
  }
  .photo--studio::before {
    content: ""; position: absolute; left: 6%; right: 6%;
    top: var(--band-top); height: var(--band-h);
    border-radius: 26px;
    background: var(--band);
    filter: blur(6px);
    -webkit-mask-image: linear-gradient(180deg, rgba(0,0,0,0.85) 0%, #000 60%, rgba(0,0,0,0.6) 100%);
            mask-image: linear-gradient(180deg, rgba(0,0,0,0.85) 0%, #000 60%, rgba(0,0,0,0.6) 100%);
  }
  .band--four-row {
    --band:
      linear-gradient(180deg, #fbfbfb 0%, #fbfbfb 38%, rgba(251,251,251,0) 58%, rgba(251,251,251,0) 84%, #f7f7f7 100%),
      linear-gradient(90deg, var(--tint-pink) 0%, var(--tint-pink) 22%, #f3f3f3 25%, var(--tint-red) 28%, var(--tint-red) 47%, #f3f3f3 51%, var(--tint-green) 54%, var(--tint-green) 73%, #f3f3f3 76%, var(--tint-blue) 79%, var(--tint-blue) 100%);
  }
  .band--four-group {
    --band:
      linear-gradient(180deg, #fbfbfb 0%, #fbfbfb 36%, rgba(251,251,251,0) 56%, rgba(251,251,251,0) 86%, #f7f7f7 100%),
      linear-gradient(90deg, var(--tint-blue) 0%, var(--tint-blue) 16%, #f3f3f3 19%, var(--tint-green) 22%, var(--tint-green) 40%, #f3f3f3 43%, var(--tint-red) 46%, var(--tint-red) 64%, #f3f3f3 67%, var(--tint-pink) 70%, var(--tint-pink) 100%);
  }

  .photo--kitchen {
    background:
      linear-gradient(90deg, rgba(0,0,0,0) 30%, rgba(245,240,238,0.75) 42%, rgba(245,240,238,0.75) 72%, rgba(0,0,0,0) 84%) 0 0 / 100% 78% no-repeat,
      linear-gradient(180deg, #5e4436 0%, #7c5e4c 45%, #8f7262 72%, #e6e2df 80%, #f4f2f1 100%);
  }
  .photo--kitchen::before {
    content: ""; position: absolute; left: 4%; right: 4%; top: 394px; height: 110px;
    border-radius: 14px; filter: blur(5px);
    background: linear-gradient(90deg, #f7f7f7 0%, var(--tint-pink) 10%, #f7f7f7 20%, var(--tint-green) 30%, #f7f7f7 40%, var(--tint-red) 50%, var(--tint-blue) 60%, #f7f7f7 70%, var(--tint-pink) 80%, #f7f7f7 90%, var(--tint-green) 100%);
    opacity: 0.9;
  }

  .ribbon {
    position: absolute; z-index: 3; display: flex; align-items: center; justify-content: center;
    font-family: "Poppins", sans-serif; font-weight: 800; color: var(--white);
    text-align: center; letter-spacing: -0.01em;
    clip-path: polygon(0 0, 100% 0, calc(100% - 14px) 50%, 100% 100%, 0 100%, 14px 50%);
  }
  .ribbon--rose-deep { background: var(--rose-deep); }
  .ribbon--mint { background: var(--mint); }
  .ribbon--rose { background: var(--rose-soft); }

  .pennant {
    position: absolute; z-index: 3; left: 16px; top: 243px; width: 131px; height: 198px;
    background: var(--mint-deep); color: var(--white);
    font-family: "Poppins", sans-serif; font-weight: 800; font-size: 52px; line-height: 1.05;
    display: flex; flex-direction: column; align-items: center; padding-top: 30px;
    clip-path: polygon(0 0, 100% 0, 100% 100%, 50% 84%, 0 100%);
  }

  .panel { position: absolute; inset: 0; }
  .panel--mint { background: var(--mint); }
  .panel--rose { background: var(--rose-soft); }
  .frame { position: absolute; border: 2px dotted rgba(255,255,255,0.85); }
  .panel-title {
    position: absolute; left: 0; width: 100%; text-align: center;
    font-family: "Jost", sans-serif; font-weight: 500; color: var(--white);
    text-transform: uppercase; white-space: nowrap;
  }
</style>
</head>
<body>
<main class="canvas">

  <section class="tile col-left row-1">
    <div class="header header--rose" style="height:168px;font-size:34px;">
      <span>Mother’s Day</span><span>Meadow Reset Sale</span>
    </div>
    <div class="photo photo--studio band--four-row" style="top:168px;--band-top:96px;--band-h:173px;" role="img" aria-label="Four supplement bottles standing in a row on a light studio surface"></div>
    <div class="ribbon ribbon--rose-deep" style="left:36px;top:505px;width:432px;height:68px;font-size:33px;">25% Off Everything!</div>
  </section>

  <section class="tile col-right row-1">
    <div class="header header--mint" style="height:99px;font-size:31px;">
      <span>Mother’s Day</span><span>Meadow Reset Sale</span>
    </div>
    <div class="photo photo--kitchen" style="top:99px;" role="img" aria-label="Smiling woman in a kitchen presenting a lineup of supplement bottles on the counter"></div>
    <div class="pennant"><span>25%</span><span>Off</span></div>
  </section>

  <section class="tile col-left row-2">
    <div class="header header--rose" style="height:198px;font-size:48px;line-height:1.2;letter-spacing:0.18em;">
      <span>25% Off All</span><span>Supplements</span>
    </div>
    <div class="photo photo--studio band--four-group" style="top:198px;--band-top:63px;--band-h:247px;" role="img" aria-label="Four supplement bottles grouped at an angle on a light studio surface"></div>
    <div class="ribbon ribbon--mint" style="left:36px;top:525px;width:432px;height:68px;font-size:31px;">Meadow Reset Sale!</div>
  </section>

  <section class="tile col-right row-2">
    <div class="panel panel--mint"></div>
    <div class="frame" style="left:14px;top:23px;width:469px;height:481px;"></div>
    <div class="panel-title" style="top:52px;font-size:44px;line-height:57px;letter-spacing:0.23em;">
      25% Off<br>Meadow<br>Reset Sale:<br>Spring Reset.
    </div>
    <div class="ribbon ribbon--rose" style="left:36px;top:414px;width:432px;height:171px;font-size:76px;line-height:1.0;">Summer<br>Ready!</div>
  </section>

  <section class="tile col-left row-3">
    <div class="panel panel--rose"></div>
    <div class="frame" style="left:15px;top:24px;width:468px;height:480px;"></div>
    <div class="panel-title" style="top:56px;font-size:58px;line-height:72px;letter-spacing:0.21em;">
      25% Off<br>Mother’s<br>Day Sale:
    </div>
    <div class="ribbon ribbon--mint" style="left:36px;top:432px;width:432px;height:147px;font-size:50px;line-height:1.25;">Feel Amazing<br>Again!</div>
  </section>

  <section class="tile col-right row-3">
    <div class="header header--rose-soft" style="height:243px;font-size:46px;line-height:56px;letter-spacing:0.2em;">
      <span>25% Off</span><span>Mother’s Day</span><span>Sale</span>
    </div>
    <div class="photo photo--studio band--four-group" style="top:243px;--band-top:18px;--band-h:250px;" role="img" aria-label="Four supplement bottles grouped at an angle on a light studio surface"></div>
    <div class="ribbon ribbon--rose-deep" style="left:36px;top:527px;width:432px;height:68px;font-size:33px;">Refresh Your Body</div>
  </section>

</main>
</body>
</html>
```